Natural Stone Company Redesign

Looking for a fresh, creative, website design. We service Luxury Residential projects in US and Internationally. We would like to see a design that communicates a passion for creative challenging design that is merged with natural stone projects. Our new company Logo is "Inspiration meets Earth"

We like to emphasis from concept to completion, for example, photos of blueprints and/or sketches of a project, then a completion photo of same project.

some websites we like are:
http://www.brelmofask.com/
http://tovanquistdesign.com/

We would like to highlight our services of "concept to completion" scenario. Blueprints/sketches to finished products.
Page needed:
Home
About Us
Projects
Contact Us

Target Market(s)

Developers, architects, designers

Industry/Entity Type

It Company

Number of Pages Required

4 page

Font styles to use
Sans Serif

Requirements
Must have
• "Inspiration Meets Earth"
• New, innovative, look.
• Something to grab the attention, and make them think
Nice to have
• Motion on the homepage
• Roll over the finished project photo, and have the name of the stone pop up

```html
<!DOCTYPE html>
<html lang="en">
<head>
<meta charset="utf-8">
<title>Strata Inc. — Inspiration Meets Earth</title>
<link rel="stylesheet" href="https://fonts.googleapis.com/css2?family=Open+Sans:wght@400;600;700;800&display=swap">
<style>
  :root{
    --orange:#f7a21b;
    --ink:#3a3a3a;
    --muted:#8a8a8a;
    --rule:#d9d9d9;
    --panel:#f0f0f0;
    --footer:#a7a9ac;
    --white:#ffffff;
    --star-off:#d9d9d9;
    --star-on:#8c8c8c;
  }
  *{box-sizing:border-box;margin:0;padding:0}
  html,body{width:1200px;height:4063px;overflow:hidden;background:var(--white)}
  body{font-family:"Open Sans",Arial,sans-serif;color:var(--ink);position:relative}
  .abs{position:absolute}

  /* header */
  .brand{left:32px;top:16px;display:flex;align-items:center;gap:10px}
  .brand-mark{width:30px;height:30px;background:var(--orange)}
  .brand-name{font-size:20px;font-weight:600;color:#555;letter-spacing:2px}
  .search{left:293px;top:11px;width:614px;height:30px;border:1px solid #d3d3d3;background:var(--white);display:flex}
  .search-field{flex:1;font-size:12px;color:#999;padding:6px 0 0;text-align:center}
  .search-btn{width:68px;background:var(--orange);display:flex;align-items:center;justify-content:center}
  .auth{left:1008px;top:11px;display:flex;gap:6px}
  .auth-btn{width:78px;height:30px;background:var(--orange);color:var(--white);font-size:13px;font-weight:600;display:flex;align-items:center;justify-content:center}
  .nav{left:0;top:46px;width:1200px;height:33px}
  .nav-item{position:absolute;top:0;height:33px;line-height:33px;font-size:12px;color:#555;text-align:center;width:68px}
  .nav-item.active{background:var(--orange);color:var(--white);font-weight:600}
  .nav-rule{left:0;top:79px;width:1200px;height:3px;background:var(--orange)}

  /* hero */
  .hero{left:32px;top:103px;width:1138px;height:490px;background:linear-gradient(160deg,#5b4a36 0%,#2f2a22 40%,#6a5a3f 70%,#3b4028 100%)}
  .hero-arrow{top:210px;color:var(--white);font-size:44px;line-height:1}
  .hero-title{left:0;top:240px;width:1138px;text-align:center;color:var(--white);font-size:58px;font-weight:700;letter-spacing:-1px;line-height:1.1;text-shadow:0 2px 6px rgba(0,0,0,.5)}
  .hero-copy{left:284px;top:328px;width:570px;text-align:center;color:var(--white);font-size:13px;line-height:1.5}
  .hero-dots{left:0;top:452px;width:1138px;display:flex;justify-content:center;gap:10px}
  .dot{width:12px;height:12px;border-radius:50%;background:rgba(255,255,255,.85)}
  .dot.on{background:var(--white);box-shadow:0 0 0 2px rgba(0,0,0,.25)}

  .rule{left:32px;width:1138px;height:1px;background:var(--rule)}
  .section-title{left:0;width:1200px;text-align:center;color:var(--orange);font-size:66px;font-weight:700;letter-spacing:-1px;line-height:1}
  .welcome-copy{left:230px;top:752px;width:740px;text-align:center;font-size:14px;line-height:1.6;color:#444}

  /* residence cards */
  .card{top:1067px;width:261px;height:491px;background:var(--panel)}
  .card-photo{height:342px}
  .card-label{height:108px;background:var(--orange);text-align:center;padding-top:30px}
  .card-name{color:var(--white);font-size:21px;font-weight:600}
  .card-stars{display:flex;justify-content:center;gap:3px;margin-top:6px}
  .card-stats{height:41px;display:flex;align-items:center;font-size:12px;color:var(--muted)}
  .stat{flex:1;display:flex;align-items:center;justify-content:center;gap:6px}
  .stat + .stat{border-left:1px solid #d6d6d6}

  /* featured */
  .feature{left:0;top:1634px;width:1200px;height:880px;background:var(--orange)}
  .feature-photo{left:38px;top:89px;width:539px;height:707px;border:7px solid var(--white);background:linear-gradient(180deg,#46506a 0%,#363f58 35%,#4a3c2c 60%,#2a241d 100%)}
  .feature-title{left:618px;top:78px;color:var(--white);font-size:68px;font-weight:700;line-height:1.25}
  .feature-stars{left:618px;top:262px;display:flex;gap:8px}
  .feature-copy{left:618px;top:560px;width:552px;font-size:13px;line-height:1.5;color:#3a2a10}
  .feature-stats{left:618px;top:753px;width:552px;height:43px;background:var(--panel);display:flex;align-items:center;font-size:13px;color:var(--muted)}

  /* services */
  .service{width:552px;background:var(--panel)}
  .service-face{height:328px;display:flex;flex-direction:column;align-items:center;padding-top:50px}
  .service-line{width:225px;height:3px;margin-top:18px}
  .service-name{font-size:56px;font-weight:800;margin-top:12px;letter-spacing:1px;line-height:1.2}
  .service-copy{padding:28px 50px 0;text-align:center;font-size:20px;line-height:1.38;color:#333}
  .bronze .service-face{background:linear-gradient(135deg,#b07a55 0%,#8a4a34 55%,#6a2623 100%)}
  .bronze .service-name{color:#d59a6c;text-shadow:0 1px 0 #6a3420}.bronze .service-line{background:#c28a60}
  .silver .service-face{background:linear-gradient(135deg,#dedbd2 0%,#a9a7a1 55%,#767675 100%)}
  .silver .service-name{color:#ececec;text-shadow:0 1px 0 #777}.silver .service-line{background:#eeeeee}
  .gold .service-face{background:linear-gradient(135deg,#fbd23a 0%,#f7a420 55%,#f28a10 100%)}
  .gold .service-name{color:#fde25a;text-shadow:0 1px 0 #c97a10}.gold .service-line{background:#fde25a}
  .platinum .service-face{background:linear-gradient(135deg,#8d9693 0%,#535d5a 55%,#2a3331 100%)}
  .platinum .service-name{color:#e8e8e8;font-size:48px;font-weight:700;margin-top:18px}.platinum .service-line{background:#dcdcdc}

  /* footer */
  .footer{left:0;top:3914px;width:1200px;height:149px;background:var(--footer);border-top:6px solid var(--orange)}
  .footer-nav{left:0;top:48px;width:1200px;display:flex;justify-content:center;gap:78px;font-size:11px;color:#333}
  .footer-rule{left:165px;top:78px;width:870px;height:1px;background:#8c8e91}
  .footer-social{left:0;top:102px;width:1200px;display:flex;justify-content:center;gap:8px}
  .social-dot{width:16px;height:16px;border-radius:3px;background:#6e7073}
</style>
</head>
<body>
<svg width="0" height="0" style="position:absolute" aria-hidden="true">
  <defs>
    <symbol id="star" viewBox="0 0 24 24"><path d="M12 2l2.9 6.6 7.1.6-5.4 4.7 1.6 7-6.2-3.7-6.2 3.7 1.6-7L2 9.2l7.1-.6z"/></symbol>
    <symbol id="heart" viewBox="0 0 24 24"><path d="M12 21l-1.4-1.3C5.4 15 2 12 2 8.2 2 5.1 4.4 3 7.3 3c1.8 0 3.5.8 4.7 2.1C13.2 3.8 14.9 3 16.7 3 19.6 3 22 5.1 22 8.2c0 3.8-3.4 6.8-8.6 11.5z"/></symbol>
    <symbol id="comment" viewBox="0 0 24 24"><path d="M3 4h13v9H8l-4 3v-3H3z"/><path d="M18 8h3v9h-1v3l-4-3h-6v-2h8z"/></symbol>
  </defs>
</svg>

<header>
  <div class="abs brand"><span class="brand-mark"></span><span class="brand-name">STRATA INC.</span></div>
  <div class="abs search">
    <div class="search-field">Looking for something?</div>
    <div class="search-btn"><svg width="16" height="16" viewBox="0 0 24 24" fill="none" stroke="#fff" stroke-width="3"><circle cx="10" cy="10" r="6"/><path d="M15 15l6 6"/></svg></div>
  </div>
  <div class="abs auth"><div class="auth-btn">Login</div><div class="auth-btn">Sign up</div></div>
  <nav class="abs nav">
    <div class="nav-item active" style="left:420px">Home</div>
    <div class="nav-item" style="left:516px">Project</div>
    <div class="nav-item" style="left:614px">About Us</div>
    <div class="nav-item" style="left:711px">Contact Us</div>
  </nav>
  <div class="abs nav-rule"></div>
</header>

<section class="abs hero" role="img" aria-label="Photo of a luxury stone courtyard home with a glass pavilion and tropical garden">
  <div class="abs hero-arrow" style="left:48px">&laquo;</div>
  <div class="abs hero-arrow" style="left:1068px">&raquo;</div>
  <h1 class="abs hero-title">INSPIRATION MEETS EARTH</h1>
  <p class="abs hero-copy">Every stone carries the story of the earth beneath it. We shape each slab with patience and care, turning quarried rock into floors, walls and courtyards that feel calm, warm and lasting. From the first sketch to the final polish, our team guides every step.</p>
  <div class="abs hero-dots"><span class="dot on"></span><span class="dot"></span><span class="dot"></span><span class="dot"></span><span class="dot"></span></div>
</section>

<div class="abs rule" style="top:618px"></div>
<h2 class="abs section-title" style="top:650px">WELCOME</h2>
<p class="abs welcome-copy">Welcome to Strata Inc. We work with developers, architects and designers on luxury homes across the country and abroad. Every project runs from concept to completion: blueprints and sketches become cut stone, and the drawing on paper becomes the room you walk through. Explore our recent residences and see how ideas meet the earth.</p>
<div class="abs rule" style="top:880px"></div>

<h2 class="abs section-title" style="top:944px">LUXURY RESIDENT</h2>

<article class="abs card" style="left:32px">
  <div class="card-photo" role="img" aria-label="Photo of Rione Resident at dusk with palm trees" style="background:linear-gradient(180deg,#56688a 0%,#3f4e6a 50%,#5a4430 100%)"></div>
  <div class="card-label"><div class="card-name">Rione Resident</div>
    <div class="card-stars"><svg width="16" height="16" fill="var(--star-on)"><use href="#star"/></svg><svg width="16" height="16" fill="var(--star-on)"><use href="#star"/></svg><svg width="16" height="16" fill="var(--star-on)"><use href="#star"/></svg><svg width="16" height="16" fill="var(--star-off)"><use href="#star"/></svg><svg width="16" height="16" fill="var(--star-off)"><use href="#star"/></svg></div></div>
  <div class="card-stats"><div class="stat"><svg width="12" height="12" fill="#999"><use href="#heart"/></svg>122</div><div class="stat"><svg width="13" height="13" fill="#999"><use href="#comment"/></svg>32</div></div>
</article>
<article class="abs card" style="left:325px">
  <div class="card-photo" role="img" aria-label="Photo of Woodcore Resident interior with timber screens" style="background:linear-gradient(180deg,#3a3324 0%,#6b5a3a 50%,#a08456 100%)"></div>
  <div class="card-label"><div class="card-name">Woodcore Resident</div>
    <div class="card-stars"><svg width="16" height="16" fill="var(--star-on)"><use href="#star"/></svg><svg width="16" height="16" fill="var(--star-on)"><use href="#star"/></svg><svg width="16" height="16" fill="var(--star-on)"><use href="#star"/></svg><svg width="16" height="16" fill="var(--star-on)"><use href="#star"/></svg><svg width="16" height="16" fill="var(--star-off)"><use href="#star"/></svg></div></div>
  <div class="card-stats"><div class="stat"><svg width="12" height="12" fill="#999"><use href="#heart"/></svg>136</div><div class="stat"><svg width="13" height="13" fill="#999"><use href="#comment"/></svg>12</div></div>
</article>
<article class="abs card" style="left:615px">
  <div class="card-photo" role="img" aria-label="Photo of Innabale Resident terrace pool overlooking the sea" style="background:linear-gradient(180deg,#ece5b4 0%,#c9b77a 45%,#7c7350 100%)"></div>
  <div class="card-label"><div class="card-name">Innabale Resident</div>
    <div class="card-stars"><svg width="16" height="16" fill="var(--star-on)"><use href="#star"/></svg><svg width="16" height="16" fill="var(--star-on)"><use href="#star"/></svg><svg width="16" height="16" fill="var(--star-on)"><use href="#star"/></svg><svg width="16" height="16" fill="var(--star-on)"><use href="#star"/></svg><svg width="16" height="16" fill="var(--star-on)"><use href="#star"/></svg></div></div>
  <div class="card-stats"><div class="stat"><svg width="12" height="12" fill="#999"><use href="#heart"/></svg>212</div><div class="stat"><svg width="13" height="13" fill="#999"><use href="#comment"/></svg>35</div></div>
</article>
<article class="abs card" style="left:907px">
  <div class="card-photo" role="img" aria-label="Photo of Ocean Scape Resident entrance with red timber and stone path" style="background:linear-gradient(160deg,#8a3a24 0%,#b0774a 45%,#6d7a52 100%)"></div>
  <div class="card-label"><div class="card-name">Ocean Scape Resident</div>
    <div class="card-stars"><svg width="16" height="16" fill="var(--star-on)"><use href="#star"/></svg><svg width="16" height="16" fill="var(--star-on)"><use href="#star"/></svg><svg width="16" height="16" fill="var(--star-on)"><use href="#star"/></svg><svg width="16" height="16" fill="var(--star-off)"><use href="#star"/></svg><svg width="16" height="16" fill="var(--star-off)"><use href="#star"/></svg></div></div>
  <div class="card-stats"><div class="stat"><svg width="12" height="12" fill="#999"><use href="#heart"/></svg>130</div><div class="stat"><svg width="13" height="13" fill="#999"><use href="#comment"/></svg>112</div></div>
</article>

<section class="abs feature">
  <div class="abs feature-photo" role="img" aria-label="Photo of Luxonia Resident at dusk with palms and a reflecting pool, the finished result of its stone blueprint"></div>
  <h2 class="abs feature-title">LUXONIA<br>RESIDENT</h2>
  <div class="abs feature-stars"><svg width="44" height="44" fill="#a8650f"><use href="#star"/></svg><svg width="44" height="44" fill="#a8650f"><use href="#star"/></svg><svg width="44" height="44" fill="#a8650f"><use href="#star"/></svg><svg width="44" height="44" fill="#a8650f"><use href="#star"/></svg><svg width="44" height="44" fill="#a8650f"><use href="#star"/></svg></div>
  <p class="abs feature-copy">Concept to completion: Luxonia began as a hand-drawn blueprint of terraces, pool edges and stone walls. Our team tested samples on site, then laid honed limestone chosen for its soft tone and cool touch under bare feet. Inside, book-matched marble panels frame the living room, while the kitchen counters use a dark granite quarried for this home alone. Every cut followed the original sketch through installation. The finished residence sits among tall palms, its reflecting pool mirroring warm lights at dusk, rooted in its land and built to last for generations.</p>
  <div class="abs feature-stats"><div class="stat"><svg width="13" height="13" fill="#999"><use href="#heart"/></svg>1208</div><div class="stat"><svg width="14" height="14" fill="#999"><use href="#comment"/></svg>780</div></div>
</section>

<h2 class="abs section-title" style="top:2572px">CHOOSE YOUR SERVICES</h2>

<article class="abs service bronze" style="left:32px;top:2698px;height:561px">
  <div class="service-face"><div><svg width="40" height="40" fill="#c28a60"><use href="#star"/></svg><svg width="54" height="54" fill="#c28a60"><use href="#star"/></svg><svg width="40" height="40" fill="#c28a60"><use href="#star"/></svg></div><div class="service-line"></div><div class="service-name">BRONZE</div></div>
  <p class="service-copy">Bronze level covers stone supply. Choose a solid slab from our stock of marble, granite and limestone, cut to your measurements. This is our basic level, suited to quick projects with a short turn around time.</p>
</article>
<article class="abs service silver" style="left:615px;top:2698px;height:561px">
  <div class="service-face"><div><svg width="40" height="40" fill="#eeeeee"><use href="#star"/></svg><svg width="54" height="54" fill="#eeeeee"><use href="#star"/></svg><svg width="40" height="40" fill="#eeeeee"><use href="#star"/></svg></div><div class="service-line"></div><div class="service-name">SILVER</div></div>
  <p class="service-copy">Silver level pairs stone supply with design advice. We review your plans and offer two stone palettes with three finishes to choose from.</p>
</article>
<article class="abs service gold" style="left:32px;top:3283px;height:550px">
  <div class="service-face"><div><svg width="40" height="40" fill="#fde25a"><use href="#star"/></svg><svg width="54" height="54" fill="#fde25a"><use href="#star"/></svg><svg width="40" height="40" fill="#fde25a"><use href="#star"/></svg></div><div class="service-line"></div><div class="service-name">GOLD</div></div>
  <p class="service-copy">Gold level turns your blueprints and sketches into finished rooms, with custom fabrication, edge details and full installation.</p>
</article>
<article class="abs service platinum" style="left:615px;top:3283px;height:550px">
  <div class="service-face"><div><svg width="40" height="40" fill="#e0e0e0"><use href="#star"/></svg><svg width="54" height="54" fill="#e0e0e0"><use href="#star"/></svg><svg width="40" height="40" fill="#e0e0e0"><use href="#star"/></svg></div><div class="service-line"></div><div class="service-name">PLATINUM</div></div>
  <p class="service-copy">Platinum level is full concept to completion: we draw the plans, source rare stone worldwide, then fabricate, install and seal every surface.</p>
</article>

<footer class="abs footer">
  <nav class="abs footer-nav"><span>Home</span><span>Project</span><span>About Us</span><span>Contact Us</span></nav>
  <div class="abs footer-rule"></div>
  <div class="abs footer-social"><span class="social-dot"></span><span class="social-dot"></span><span class="social-dot"></span><span class="social-dot"></span><span class="social-dot"></span></div>
</footer>
</body>
</html>
```